Heron Freightlines needs Bussiness cards!

Our new trucking company needs business cards!
We need the same design with two different names and emails, everything else it's the same.
I have included our original logo so we can use it for the design.
Note: the logo to be used is the o e with the buffalo on the right side, next to the letters H and F.

Target Market(s)

Trucking, refrigerated transportation, freight

Industry/Entity Type

Business

Contact Information for Business Card

Card #1:
Marcus Tellwright
marcustellwright@heronfreightlines.example
1-844-555-0193
(956)555-0178
3817 W. Tarrow Ave.
Pharr, TX 78599
www.heronfreightlines.example

Card#2:
Orla Brennick
orla@heronfreightlines.example
1-844-555-0193
(956)555-0178
3817 W. Tarrow Ave.
Pharr, TX 78599
www.heronfreightlines.example

Font styles to use
Sans Serif

Colors
0655a3
ec1f27
ffffff

Requirements
Must have
• our logo
Nice to have
• roads on background,

```html
<!DOCTYPE html>
<html lang="en">
<head>
<meta charset="utf-8">
<title>Heron Freightlines — Business Cards</title>
<link href="https://fonts.googleapis.com/css2?family=Roboto:wght@400;500;900&display=swap" rel="stylesheet">
<style>
  :root {
    --brand-blue: #0655a3;
    --brand-navy: #0b3f80;
    --brand-red: #ec1f27;
    --white: #ffffff;
    --card-light: #f7f7f8;
    --card-shade: #e4e5e8;
    --text-dark: #1d1f24;
    --stage: #d9d6d0;
  }
  * { margin: 0; padding: 0; box-sizing: border-box; }
  html, body {
    width: 1200px; height: 1023px; overflow: hidden;
    background: var(--stage);
    font-family: "Roboto", Arial, sans-serif;
  }
  .sheet {
    position: relative; width: 1200px; height: 1023px;
    display: flex; align-items: center; justify-content: center; gap: 40px;
  }
  .card {
    position: relative; width: 540px; height: 309px;
    border-radius: 16px; overflow: hidden;
    box-shadow: 0 10px 28px rgba(0,0,0,.18);
  }

  /* Front */
  .card-front {
    background: linear-gradient(135deg, var(--white) 0%, var(--card-light) 55%, var(--card-shade) 100%);
  }
  .card-front .swoosh { position: absolute; inset: 0; }
  .wordmark {
    position: absolute; display: flex; align-items: center; gap: 10px;
    font-weight: 900; color: var(--brand-red); white-space: nowrap;
  }
  .card-front .wordmark { left: 30px; top: 40px; font-size: 30px; }
  .wordmark .mark-dot {
    width: 22px; height: 22px; border-radius: 50%; background: var(--brand-blue);
    flex: none;
  }
  .holder-name {
    position: absolute; left: 32px; top: 118px;
    font-size: 22px; font-weight: 400; color: var(--brand-red);
  }
  .contact-list {
    position: absolute; left: 32px; top: 158px; list-style: none;
    font-size: 13px; color: var(--text-dark); line-height: 25px;
  }
  .contact-list li { display: flex; align-items: center; gap: 9px; }
  .contact-list svg { width: 15px; height: 15px; flex: none; }
  .website {
    position: absolute; right: 22px; bottom: 20px;
    font-size: 12px; color: var(--brand-red);
  }

  /* Back */
  .card-back { background: var(--card-light); }
  .road-photo {
    position: absolute; inset: 0;
    background:
      radial-gradient(ellipse at 85% 70%, rgba(240,190,120,.55), transparent 55%),
      linear-gradient(180deg, #e9e9ea 0%, #d8d6d2 60%, #c9c2b8 100%);
    opacity: .85;
  }
  .card-back .bands { position: absolute; inset: 0; }
  .card-back .wordmark {
    left: 50%; top: 50%; transform: translate(-50%, -50%); font-size: 34px;
  }
  .card-back .wordmark .mark-dot { width: 26px; height: 26px; }
</style>
</head>
<body>
<main class="sheet">

  <section class="card card-front" aria-label="Business card front">
    <svg class="swoosh" viewBox="0 0 540 309" aria-hidden="true">
      <path d="M330 309 C 360 200, 420 90, 540 40 L 540 52 C 430 100, 378 205, 350 309 Z" fill="var(--brand-navy)"/>
    </svg>
    <div class="wordmark"><span class="mark-dot"></span>Heron Freightlines</div>
    <p class="holder-name">Marcus Tellwright</p>
    <ul class="contact-list">
      <li>
        <svg viewBox="0 0 16 16"><circle cx="8" cy="8" r="8" fill="var(--brand-red)"/><path d="M8 3.5a3 3 0 0 0-3 3c0 2.2 3 5.5 3 5.5s3-3.3 3-5.5a3 3 0 0 0-3-3zm0 4.2a1.2 1.2 0 1 1 0-2.4 1.2 1.2 0 0 1 0 2.4z" fill="var(--white)"/></svg>
        3817 W. Tarrow Ave. Pharr, TX 78599
      </li>
      <li>
        <svg viewBox="0 0 16 16"><rect width="16" height="16" rx="3" fill="var(--brand-red)"/><path d="M5 3.5l2 2-1 1.2c.6 1.3 1.6 2.3 2.9 2.9l1.2-1 2 2-1.3 1.4C7.5 11.8 4.2 8.5 3.6 5z" fill="var(--white)"/></svg>
        1-844-555-0193
      </li>
      <li>
        <svg viewBox="0 0 16 16"><rect x="4" y="1" width="8" height="14" rx="1.5" fill="none" stroke="var(--brand-red)" stroke-width="1.4"/><circle cx="8" cy="12.5" r=".9" fill="var(--brand-red)"/></svg>
        (956)555-0178
      </li>
      <li>
        <svg viewBox="0 0 16 16"><rect x="1" y="3" width="14" height="10" fill="none" stroke="var(--brand-red)" stroke-width="1.3"/><path d="M1 3l7 6 7-6M1 13l5-5M15 13l-5-5" fill="none" stroke="var(--brand-red)" stroke-width="1.1"/></svg>
        marcustellwright@heronfreightlines.example
      </li>
    </ul>
    <p class="website">www.heronfreightlines.example</p>
  </section>

  <section class="card card-back" aria-label="Business card back">
    <div class="road-photo" role="img" aria-label="Photo of a highway at dusk with light trails and trees"></div>
    <svg class="bands" viewBox="0 0 540 309" aria-hidden="true">
      <polygon points="470,0 500,0 430,309 400,309" fill="var(--brand-navy)"/>
      <polygon points="510,0 540,0 540,20 476,309 446,309" fill="var(--brand-navy)"/>
      <polygon points="540,70 540,309 486,309" fill="var(--brand-red)"/>
    </svg>
    <div class="wordmark"><span class="mark-dot"></span>Heron Freightlines</div>
  </section>

</main>
</body>
</html>
```